E-Book-Cover für Ratgeber zum Thema Weisheit
Der Designer "kreidler" hat das Kunststück vollbracht, schon mit seinem ersten Entwurf genau ins Schwarze zu treffen, sodass nur noch Feinheiten abgestimmt werden mussten. Nach kleinen Wartezeiten ging er auf meine Wünsche ein und lieferte ein optimales Ergebnis ab, ohne dabei viele Worte zu verlieren. Er übermittelte mir eine farbige und eine schwarzweiße Variante des Designs in verschiedenen Dateiformaten. Ich kann diesen Designer nur empfehlen und würde wieder mit ihm arbeiten.
Zielgruppe
Ich bin ein experimenteller Schriftsteller, der ein E-Book über Folio Rapid Verlag auf Bornix veröffentlichen möchte. Das Thema des Ratgebers ist Weisheit.
Weisheit gilt als ein eher antiquierter und abstrakter Begriff. Das ist ein Irrtum. Sie ist wichtiger als je zuvor und kann beschrieben werden. Weder ist sie gleichzusetzen mit Klugheit, noch mit spiritueller Erleuchtung. Sie beinhaltet bestimmte Eigenschaften wie Vernunft, Wissbegierde, Demut, Einfühlungsvermögen, Intuition, Auflehnung... Wobei rationales Denken das oberste Gebot ist. Es wird u.a. gezeigt, was Weisheit für das eigene Leben bringt und wie man sie anstreben kann.
Die Zielgruppe sind alle Menschen, die an Philosophie, Psychologie, Selbstoptimierung oder Religionen bzw. Atheismus interessiert sind. Menschen, die nach einer Erkenntnis oder 'Erleuchtung' suchen und etwas Besonderes in der Bücherflut entdecken möchten. Es ist weniger für Akademiker geschrieben; eher für die 'normale', durchschnittliche Bevölkerung und kann auch von bildungsferneren Schichten aller Altersgruppen verstanden werden.
Meine Vermutung ist, dass es bei offenen Personen mittleren Alters Anklang finden könnte.
Aufgabenstellung
Der Titel und der Untertitel des Buches müssen vorkommen (Titel: 'Das Helle Ufer'; Untertitel: 'Wie Sie mit dem revolutionären Konzept der modernen Weisheit wahre Größe erlangen'). Außerdem soll ein runder Button/Aufkleber/Sticker auf dem Cover kleben, welcher folgenden Text enthält: 'Mit Selbsttest! Wie weise bin ich?').
Natürlich soll der Name des Autors ebenfalls vorkommen: 'Malte Brunsig'
Das Cover soll sehr aus der Masse herausstechen, demnach ein echter Hingucker sein. Der potenzielle Kunde soll sofort neugierig sein! Es muss sowohl klein (als Thumbnail und am Smartphone), als auch groß gut aussehen und der Titel stets gut lesbar sein. Außerdem muss es schwarzweiß gut aussehen und erkennbar sein (für ebook-reader).
Bornix gibt folgende Werte für die Bilddatei vor: Die idealen Abmessungen für Coverdateien liegen bei 2 560 x 1 600 Pixeln. Mindestens 300 dpi. Die Größe der Bilddatei sollte 50MB nicht übersteigen. Farbprofil: RGB. DATEIFORMAT: JPG oder TIFF
Coverbilder mit weißem oder sehr hellem Hintergrund heben sich kaum vom Hintergrund ab. Fügen Sie einen dünnen Rahmen (3–4 Pixel) in Mittelgrau hinzu, um die Ränder des Coverbilds besser sichtbar zu machen.
Welches Cover gut zum Thema Weisheit passt, überlasse ich Ihrer Genialität. Ich dachte vielleicht an eine Art Blitz, Supernova, Erleuchtung, Explosion, geometrische Form o.ä. Aber Sie können sich etwas ganz eigenes ausdenken. Es sollte eher abstrakt sein. Außerdem muss es klar, edel und modern wirken, weniger comichaft oder verspielt/kitschig. Es darf etwas aggressiv bzw. 'revolutionär' wirken.

```html
<!DOCTYPE html>
<html lang="de">
<head>
<meta charset="utf-8">
<title>Das Helle Ufer – Malte Brunsig</title>
<link rel="stylesheet" href="https://fonts.googleapis.com/css2?family=Jost:wght@300;500&family=Carlito:ital,wght@0,400;0,700;1,700&display=swap">
<style>
  :root {
    --sky-deep: #6f9fd6;
    --sky-mid: #8fd0f2;
    --glow: #ffffff;
    --city-blue: #4f86c2;
    --city-haze: #a9c8e4;
    --warm-haze: #f6dcc0;
    --type-white: #ffffff;
    --type-dark: #262633;
    --sticker: #8080b2;
  }
  * { margin: 0; padding: 0; box-sizing: border-box; }
  html, body { width: 750px; height: 1200px; overflow: hidden; background: #fff; }
  .cover {
    position: relative;
    width: 750px;
    height: 1200px;
    overflow: hidden;
    font-family: "Carlito", "Calibri", sans-serif;
  }
  .cover-art {
    position: absolute;
    inset: 0;
    background:
      radial-gradient(ellipse 360px 420px at 380px 600px, var(--glow) 0%, rgba(255,255,255,0.85) 35%, rgba(255,255,255,0) 75%),
      radial-gradient(ellipse 220px 200px at 40px 860px, var(--warm-haze) 0%, rgba(246,220,192,0) 80%),
      linear-gradient(180deg, var(--sky-deep) 0%, var(--sky-mid) 30%, #d8f0fb 50%, var(--city-haze) 72%, var(--city-blue) 100%);
  }
  .title {
    position: absolute;
    top: 34px;
    left: 0;
    width: 750px;
    text-align: center;
    font-family: "Jost", "Futura", sans-serif;
    font-weight: 300;
    font-size: 138px;
    line-height: 104px;
    color: var(--type-white);
    letter-spacing: 2px;
  }
  .title span { display: block; }
  .author {
    position: absolute;
    top: 276px;
    left: 0;
    width: 750px;
    text-align: center;
    font-family: "Jost", "Futura", sans-serif;
    font-weight: 500;
    font-size: 41px;
    letter-spacing: 1px;
    color: var(--type-white);
  }
  .sticker {
    position: absolute;
    left: 19px;
    top: 365px;
    width: 178px;
    height: 178px;
    border-radius: 50%;
    background: var(--sticker);
    color: var(--type-white);
    display: flex;
    flex-direction: column;
    align-items: center;
    justify-content: center;
    text-align: center;
    transform: rotate(-7deg);
    padding-bottom: 6px;
  }
  .sticker-kicker { font-weight: 700; font-size: 21px; line-height: 25px; }
  .sticker-question { font-weight: 700; font-style: italic; font-size: 30px; line-height: 36px; margin-top: 2px; }
  .subtitle {
    position: absolute;
    top: 980px;
    left: 0;
    width: 764px;
    text-align: center;
    font-weight: 700;
    font-size: 33px;
    line-height: 42px;
    color: var(--type-dark);
  }
  .subtitle em { font-style: italic; color: var(--type-white); }
</style>
</head>
<body>
  <main class="cover">
    <div class="cover-art" role="img" aria-label="Abstrakte Lichtexplosion in Blau und Weiß mit Strahlen über einer Stadtsilhouette; ein Mann im Anzug steht von hinten gesehen auf einem Steg und blickt ins Licht"></div>

    <h1 class="title"><span>DAS HELLE</span><span>UFER</span></h1>
    <p class="author">MALTE BRUNSIG</p>

    <div class="sticker">
      <span class="sticker-kicker">Mit<br>Selbsttest!</span>
      <span class="sticker-question">“Wie weise<br>bin ich?”</span>
    </div>

    <p class="subtitle">
      Wie Sie mit dem<br>
      <em>revolutionären Konzept</em><br>
      der <em>modernen Weisheit</em><br>
      <em>wahre Größe</em> erlangen
    </p>
  </main>
</body>
</html>
```